Oakfield crest Letter head

Need a heeder and footer for 8.5 x 11 paper
2 inch top header, 1.5 inch bottom footer
Add logo, agent pictures, names and titles (Broker), office picture with address
Oakfield Crest Real Estate
28317 Route 412
Bayview Shoals, SC 29990
Please make phone # large (555) 382-0617
OakfieldCrestRealEstate.com

```html
<!DOCTYPE html>
<html lang="en">
<head>
<meta charset="utf-8">
<title>Oakfield Crest Real Estate – Letterhead</title>
<link rel="stylesheet" href="https://fonts.googleapis.com/css2?family=Open+Sans:wght@400;600&family=Roboto:wght@400;500&family=Roboto+Slab:wght@700&family=Montserrat:wght@700&display=swap">
<style>
  :root {
    --backdrop: #ebe8e3;
    --paper: #ffffff;
    --paper-shade: #f1f1f2;
    --ink: #3b3b3b;
    --ink-soft: #4a4a4a;
    --brand-red: #c4202b;
    --brand-navy: #1f2a5c;
    --photo-top: #e8d9b9;
    --photo-mid: #c9a86f;
    --photo-base: #e23a57;
  }
  * { margin: 0; padding: 0; box-sizing: border-box; }
  html, body { width: 1084px; height: 1200px; overflow: hidden; }
  body { background: var(--backdrop); position: relative; }

  .letterhead {
    position: absolute; left: 102px; top: 30px;
    width: 879px; height: 1140px;
    background: linear-gradient(180deg, var(--paper) 0%, var(--paper-shade) 19%, var(--paper) 23%, var(--paper) 60%, var(--paper-shade) 100%);
    box-shadow: 0 2px 10px rgba(0,0,0,0.18);
    overflow: hidden;
  }

  .brand {
    position: absolute; left: 86px; top: 160px;
    display: flex; align-items: center; gap: 10px;
  }
  .brand__mark { width: 18px; height: 18px; background: var(--brand-red); }
  .brand__name {
    font-family: "Montserrat", sans-serif; font-weight: 700;
    font-size: 21px; color: var(--brand-navy); letter-spacing: 0.3px;
  }

  .contact {
    position: absolute; left: 558px; top: 91px;
    font-family: "Roboto", sans-serif; font-size: 15px; line-height: 19.6px;
    color: var(--ink-soft); font-style: normal;
  }
  .contact__label { color: var(--brand-red); font-weight: 500; }

  .letter {
    position: absolute; left: 78px; top: 263px; width: 719px;
    font-family: "Open Sans", sans-serif; font-size: 15.8px; line-height: 21.8px;
    color: var(--ink);
  }
  .letter__salutation { margin-bottom: 21px; }
  .letter__body p { text-align: justify; hyphens: auto; margin-bottom: 22px; }
  .letter__closing { margin-top: 10px; }
  .letter__signature {
    display: block; margin-top: 20px; width: 100px; height: 90px;
  }

  .footer__rule {
    position: absolute; left: 0; top: 1122px; width: 660px; height: 15px;
    background: var(--brand-red);
  }
  .footer__photo {
    position: absolute; left: 713px; top: 973px; width: 138px; height: 130px;
  }
  .footer__tag {
    position: absolute; left: 632px; top: 1103px; width: 247px; height: 37px;
  }
  .footer__name {
    position: absolute; left: 670px; top: 1103px; width: 209px; height: 37px;
    display: flex; align-items: center; justify-content: center;
    font-family: "Roboto Slab", serif; font-weight: 700; font-size: 13px;
    color: #ffffff; letter-spacing: 0.3px;
  }
</style>
</head>
<body>
  <main class="letterhead">
    <header>
      <div class="brand">
        <span class="brand__mark"></span>
        <span class="brand__name">Oakfield Crest</span>
      </div>
      <address class="contact">
        Oakfield Crest Real Estate<br>
        28317 Route 412<br>
        Bayview Shoals, SC 29990<br>
        <span class="contact__label">P :</span> (555) 382-0617<br>
        <span class="contact__label">W :</span> OakfieldCrestRealEstate.com
      </address>
    </header>

    <section class="letter" lang="la">
      <p class="letter__salutation" lang="en">Dear customer,</p>
      <div class="letter__body">
        <p>Lorem ipsum dolor sit amet, consectetur adipisicing elit, sed do eiusmod tempor incididunt ut labore et dolore magna aliqua. Ut enim ad minim veniam, quis nostrud exercitation ullamco laboris nisi ut aliquip ex ea commodo consequat. Duis aute irure dolor in reprehenderit in voluptate velit esse cillum dolore eu fugiat nulla pariatur. Excepteur sint occaecat cupidatat non proident, sunt in culpa qui officia deserunt mollit anim id est laborum.</p>
        <p>Lorem ipsum dolor sit amet, consectetur adipisicing elit, sed do eiusmod tempor incididunt ut labore et dolore magna aliqua. Ut enim ad minim veniam, quis nostrud exercitation ullamco laboris nisi ut aliquip ex ea commodo consequat. Duis aute irure dolor in reprehenderit in voluptate velit esse cillum dolore eu fugiat nulla pariatur. Excepteur sint occaecat cupidatat non proident, sunt in culpa qui officia deserunt mollit anim id est laborum.</p>
        <p>Lorem ipsum dolor sit amet, consectetur adipisicing elit, sed do eiusmod tempor incididunt ut labore et dolore magna aliqua. Ut enim ad minim veniam, quis nostrud exercitation ullamco laboris nisi ut aliquip ex ea commodo consequat. Duis aute irure dolor in reprehenderit in voluptate velit esse cillum dolore eu fugiat nulla pariatur. Excepteur sint occaecat cupidatat non proident, sunt in culpa qui officia deserunt mollit anim id est laborum.</p>
        <p>Lorem ipsum dolor sit amet, consectetur adipisicing elit, sed do eiusmod tempor incididunt ut labore et dolore magna aliqua. Ut enim ad minim veniam, quis nostrud exercitation ullamco laboris nisi ut aliquip ex ea commodo consequat. Duis aute irure dolor in reprehenderit.</p>
      </div>
      <p class="letter__closing" lang="en">Yours Sincerely,</p>
      <svg class="letter__signature" role="img" aria-label="Handwritten signature" viewBox="0 0 100 90">
        <rect width="100" height="90" fill="#e6e6e6"/>
      </svg>
    </section>

    <footer>
      <div class="footer__rule"></div>
      <svg class="footer__photo" role="img" aria-label="Portrait photo of the broker" viewBox="0 0 138 130">
        <defs>
          <linearGradient id="portraitTone" x1="0" y1="0" x2="0" y2="1">
            <stop offset="0" stop-color="#eee6d6"/>
            <stop offset="0.6" stop-color="#d2b27a"/>
            <stop offset="0.8" stop-color="#e23a57"/>
            <stop offset="1" stop-color="#e23a57"/>
          </linearGradient>
        </defs>
        <rect width="138" height="130" fill="url(#portraitTone)" opacity="0.85"/>
      </svg>
      <svg class="footer__tag" viewBox="0 0 247 37" preserveAspectRatio="none" aria-hidden="true">
        <polygon points="18,0 247,0 247,37 0,37" fill="#1f2a5c"/>
      </svg>
      <div class="footer__name">Dana Whitlock - Broker</div>
    </footer>
  </main>
</body>
</html>
```